you can visit www.brisa-tostada.com and www.instagram.com\brisatostada

www.nuevosendero.co
www.instagram.com\nsdv.co

combining this 2 business into one company website

### 1. **Home Page:**
- **Company Overview:** Briefly introduce Brisa Tostada, highlight your mission and values.
- **Navigation Menu:** Links to About Us, Events, Catering, Menu, and Contact Us.
- **Dynamic Banner:** Showcase specials, events, and new updates.

### 2. **About Us Page:**
- **History:** Share your story, how you started, and your journey.
- **Team:** Introduce your key team members with photos and bios.

### 3. **Events Page:**
- **Dynamic Calendar:** Integrate Google Calendar to showcase events and schedules.
- **Event Details:** Detailed descriptions of upcoming events with images and RSVP options.

### 4. **Catering Page:**
- **Booking Form:** A user-friendly form for booking catering services.
- **Packages & Pricing:** Clearly list your catering packages and pricing.
- **Testimonials:** Showcase positive reviews from previous clients.

### 5. **Menu Page:**
- **Online Order:** Embed or redirect to your Square online order menu for easy access.
- **Menu Sections:** Categorize your menu items (e.g., Appetizers, Main Course, Desserts).

### 6. **Contact Us Page:**
- **Contact Form:** Simple form for inquiries and feedback.
- **Location & Hours:** Display your location on Google Maps and list your operating hours.
- **Social Media Links:** Integrate links to your Instagram and other social platforms.

### 7. **Responsive Design:**
- Ensure the website is mobile-friendly and responsive on all devices.

### 8. **SEO Optimization:**
- Use relevant keywords and meta tags to improve search engine ranking. optimize seo and google analytics , google reviews embedded

### 9. **Social Media Integration:**
- Add social media icons that link directly to your Instagram and other platforms.

### 10. **Security:**
- Ensure your website has SSL certification

```html
<!DOCTYPE html>
<html lang="en">
<head>
<meta charset="utf-8">
<title>Brisa Tostada – Catering, Events &amp; Menu</title>
<link rel="stylesheet" href="https://fonts.googleapis.com/css2?family=Bowlby+One&family=Poppins:wght@400;500;600;700&family=Yellowtail&display=swap">
<style>
:root{
  --red:#e31b23;
  --red-dark:#b5121a;
  --black:#111111;
  --charcoal:#1c1c1c;
  --white:#ffffff;
  --grey:#6b6b6b;
  --light:#f3f3f3;
  --yellow:#f6c21a;
  --line:#e2e2e2;
}
*{box-sizing:border-box;margin:0;padding:0}
html,body{width:1200px;height:4864px;overflow:hidden}
body{font-family:"Poppins",sans-serif;color:var(--black);background:var(--white);position:relative}
.display{font-family:"Bowlby One",sans-serif;font-weight:400;text-transform:none}
.red{color:var(--red)}
.btn{display:inline-block;border:2px solid var(--black);background:var(--white);color:var(--black);font:600 13px "Poppins",sans-serif;padding:11px 22px;letter-spacing:.5px;text-transform:uppercase}
.btn--light{border-color:var(--white);background:transparent;color:var(--white)}
.btn--red{background:var(--red);border-color:var(--red);color:var(--white)}

/* header */
.site-header{position:absolute;top:0;left:0;width:1200px;height:72px;background:var(--white);display:flex;align-items:center;padding:0 60px 0 112px}
.brand{font:700 15px "Poppins",sans-serif;color:var(--red);display:flex;align-items:center;gap:8px;width:250px}
.brand__dot{width:14px;height:14px;border-radius:50%;background:var(--red)}
.main-nav{display:flex;gap:26px;margin-left:112px;font:600 13px "Poppins",sans-serif}
.main-nav span::after{content:" ▾";font-size:9px}
.main-nav span.plain::after{content:""}
.header-actions{margin-left:auto;display:flex;align-items:center;gap:22px}
.header-actions .btn{padding:9px 22px;font-size:12px}

/* hero */
.hero{position:absolute;top:72px;left:0;width:1200px;height:696px;background:linear-gradient(90deg,#141414 0%,#1d1d1d 35%,#2a1a12 60%,#3a2414 100%);overflow:hidden}
.hero__photo{position:absolute;left:430px;top:0;width:770px;height:696px;background:radial-gradient(ellipse at 45% 45%,#b5541c 0%,#7a2e10 35%,#2b1a12 70%,transparent 100%)}
.hero__text{position:absolute;left:82px;top:200px;color:var(--white)}
.hero__title{font-size:94px;line-height:88px;letter-spacing:1px}
.hero__script{font-family:"Yellowtail",cursive;color:var(--red);font-size:34px;position:absolute;left:-10px;top:156px;transform:rotate(-90deg);transform-origin:left top}
.hero__sub{font-size:22px;margin-top:12px}
.price-badge{position:absolute;left:1020px;top:220px;width:140px;height:140px;border-radius:50%;background:var(--yellow);border:5px solid var(--white);display:flex;flex-direction:column;align-items:center;justify-content:center;color:var(--black)}
.price-badge b{font:400 26px "Bowlby One",sans-serif;line-height:28px}
.price-badge span{font:700 24px "Poppins",sans-serif}
.hero__dots{position:absolute;left:82px;top:652px;display:flex;gap:10px}
.hero__dots i{width:10px;height:10px;border-radius:50%;background:#777}
.hero__dots i:first-child{background:var(--red)}

/* about */
.about{position:absolute;top:768px;left:0;width:1200px;height:520px}
.about__mark{position:absolute;left:150px;top:90px;width:420px;height:340px;display:flex;align-items:center;gap:24px}
.about__mark i{width:90px;height:90px;border-radius:50%;background:var(--red);flex:none}
.about__mark span{font:400 56px/64px "Bowlby One",sans-serif;color:var(--black)}
.about__body{position:absolute;left:644px;top:142px;width:460px}
.about__body h2{font-size:36px;line-height:40px}
.about__body p{font-size:13px;line-height:20px;color:var(--grey);margin-top:18px}
.about__body .btn{margin-top:26px}

/* menu */
.menu{position:absolute;top:1300px;left:0;width:1200px;height:700px}
.section-title{font-size:46px;text-align:center;line-height:56px}
.menu__tabs{display:flex;justify-content:center;gap:40px;margin-top:40px;font:600 13px "Poppins",sans-serif;text-transform:uppercase}
.menu__tabs span.active{color:var(--red);border-bottom:2px solid var(--red);padding-bottom:6px}
.menu__track{position:absolute;top:178px;left:88px;display:flex;gap:28px}
.dish{width:240px;height:380px;background:var(--white);box-shadow:0 4px 18px rgba(0,0,0,.12);position:relative}
.dish__img{height:180px}
.dish__body{padding:16px}
.dish__body h3{font:400 18px "Bowlby One",sans-serif}
.dish__body p{font-size:11px;line-height:16px;color:var(--grey);margin-top:8px}
.dish__price{position:absolute;left:16px;bottom:22px;font:700 15px "Poppins",sans-serif;color:var(--red)}
.dish__go{position:absolute;right:16px;bottom:16px;width:34px;height:34px;border-radius:50%;background:var(--black);display:flex;align-items:center;justify-content:center}
.menu__cta{position:absolute;top:612px;left:0;width:1200px;text-align:center}

/* order online */
.order{position:absolute;top:2032px;left:0;width:1200px;height:540px;background:linear-gradient(90deg,#161616,#222 55%,#1a1a1a);color:var(--white);overflow:hidden}
.order__text{position:absolute;left:82px;top:130px;width:430px}
.order__text h2{font-size:72px;line-height:74px}
.order__text h3{font:400 28px "Bowlby One",sans-serif;margin-top:2px}
.order__text p{font-size:13px;line-height:20px;color:#cfcfcf;margin-top:20px}
.order__text .btn{margin-top:24px}
.order__photo{position:absolute;left:520px;top:40px;width:640px;height:460px;border-radius:50%;background:radial-gradient(ellipse at center,#c2611f 0%,#8c3a13 40%,#3a2518 70%,transparent 100%)}
.off-badge{position:absolute;left:1050px;top:360px;width:120px;height:120px;border-radius:50%;background:var(--black);border:3px solid var(--white);display:flex;flex-direction:column;align-items:center;justify-content:center;font:400 26px/28px "Bowlby One",sans-serif}
.off-badge small{font-size:18px}

/* occasion */
.occasion{position:absolute;top:2640px;left:0;width:1200px;height:580px}
.occasion__photo{position:absolute;left:120px;top:20px;width:480px;height:480px;border-radius:50%;background:radial-gradient(circle at 45% 40%,#c9954a 0%,#6b3d1e 45%,#2c1b12 100%)}
.occasion__body{position:absolute;left:652px;top:36px;width:460px}
.occasion__body h2{font-size:34px;line-height:40px}
.occasion__body p{font-size:13px;line-height:20px;color:var(--grey);margin-top:16px}
.occasion__list{list-style:none;font-size:13px;line-height:21px;margin-top:12px}
.occasion__list li.strong{font-weight:700}
.occasion__body .btn{margin-top:22px}

/* events */
.events{position:absolute;top:3236px;left:0;width:1200px;height:690px}
.events__intro{width:560px;margin:14px auto 0;text-align:center;font-size:13px;line-height:20px;color:var(--grey)}
.events__grid{position:absolute;top:160px;left:112px;display:flex;gap:40px}
.post{width:296px}
.post__img{height:210px;position:relative}
.post__tag{position:absolute;left:12px;bottom:-12px;background:var(--red);color:var(--white);font:600 11px "Poppins",sans-serif;padding:4px 12px;text-transform:uppercase}
.post__meta{display:flex;gap:22px;font-size:11px;color:var(--grey);margin-top:24px}
.post h3{font:400 18px "Bowlby One",sans-serif;margin-top:10px}
.post p{font-size:12px;line-height:18px;color:var(--grey);margin-top:8px}
.post p b{color:var(--black);font-size:11px}
.events__cta{position:absolute;top:624px;left:0;width:1200px;text-align:center}

/* instagram */
.social{position:absolute;top:3980px;left:0;width:1200px;height:470px}
.social__text{position:absolute;left:120px;top:30px;width:420px}
.social__text h2{font-size:40px;line-height:46px}
.social__text p{font-size:13px;line-height:20px;color:var(--grey);margin-top:16px}
.handle{display:flex;align-items:center;gap:12px;font:700 20px "Poppins",sans-serif;margin-top:16px}
.handle i{width:28px;height:28px;background:var(--black);border-radius:7px}
.social__phones{position:absolute;left:580px;top:10px;width:520px;height:440px;background:radial-gradient(ellipse at 55% 50%,#e8e8e8 0%,#b9b9b9 45%,#ffffff 78%)}

/* footer */
.site-footer{position:absolute;top:4460px;left:0;width:1200px;height:404px;background:var(--black);color:var(--white)}
.footer__cols{position:absolute;top:72px;left:88px;display:flex;gap:56px}
.footer__col{width:220px}
.footer__col h4{font:400 18px "Bowlby One",sans-serif;margin-bottom:14px}
.footer__col p{font-size:11px;line-height:18px;color:#cfcfcf}
.footer__col p b{color:var(--white)}
.socials{display:flex;gap:10px;margin-top:20px}
.socials i{width:34px;height:34px;border-radius:50%;background:var(--red)}
.subscribe{display:flex;flex-direction:column;gap:10px;margin-top:14px}
.subscribe span{display:block;height:34px;background:var(--white);color:var(--grey);font-size:11px;padding:9px 12px}
.subscribe b{display:block;height:34px;background:var(--red);text-align:center;font-size:12px;line-height:34px}
.cards{display:grid;grid-template-columns:repeat(4,36px);gap:8px}
.cards i{height:24px;background:#e9e9e9;border-radius:3px}
.footer__bar{position:absolute;bottom:0;left:0;width:1200px;height:56px;border-top:1px solid #333;text-align:center;font-size:11px;line-height:56px;color:#cfcfcf;letter-spacing:.5px}
</style>
</head>
<body>

<header class="site-header">
  <div class="brand"><i class="brand__dot"></i>Brisa Tostada</div>
  <nav class="main-nav">
    <span>ABOUT US</span><span>EVENTS</span><span>CATERING</span><span>MENU</span><span class="plain">CONTACT US</span>
  </nav>
  <div class="header-actions">
    <span class="btn btn--red">Order Now</span>
    <svg width="22" height="22" viewBox="0 0 24 24" fill="none" stroke="#111" stroke-width="2"><circle cx="12" cy="8" r="4"/><path d="M4 21c0-4 4-6 8-6s8 2 8 6"/></svg>
    <svg width="24" height="22" viewBox="0 0 26 24" fill="none" stroke="#111" stroke-width="2"><path d="M1 2h4l3 13h13l3-9H7"/><circle cx="10" cy="20" r="2"/><circle cx="19" cy="20" r="2"/></svg>
  </div>
</header>

<section class="hero">
  <div class="hero__photo" role="img" aria-label="Grilled chicken drumsticks with herbs and peppers on a dark board"></div>
  <div class="hero__text">
    <h1 class="hero__title display">MAKE<br>YOUR<br>EVENT</h1>
    <span class="hero__script">Chilled</span>
    <p class="hero__sub display">Flavorful Book Catering Today!</p>
  </div>
  <div class="price-badge"><b>CAD</b><span>$15.25</span></div>
  <div class="hero__dots"><i></i><i></i><i></i></div>
</section>

<section class="about">
  <div class="about__mark"><i></i><span>Brisa<br>Tostada</span></div>
  <div class="about__body">
    <h2 class="display">Your Destination for<br>Authentic <span class="red">Flavors</span></h2>
    <p>We're dedicated to bringing you authentic, handcrafted dishes that celebrate heritage and flavor. From golden baked empanadas to delightful desserts, every item on our menu is made with love and the finest ingredients.</p>
    <p>Whether you're stopping by for a quick bite, planning a grand event, or looking for catering services, we're here to create unforgettable experiences for every occasion.</p>
    <span class="btn">Learn More</span>
  </div>
</section>

<section class="menu">
  <h2 class="section-title display">Discover the <span class="red">Menu</span></h2>
  <div class="menu__tabs">
    <span class="active">All</span><span>Crispy</span><span>Grilled</span><span>Ramen</span><span>Catering</span><span>Baked Empanada</span><span>Frozen Empanada</span><span>Baked Pastries</span>
  </div>
  <div class="menu__track">
    <article class="dish">
      <div class="dish__img" role="img" aria-label="Crispy fried pork belly with dipping sauce" style="background:linear-gradient(135deg,#c9772e,#7a3a14)"></div>
      <div class="dish__body"><h3>Lechon Kawali</h3><p>Grilled and crispy pork combined, seasoned with a blend of spices and herbs.</p></div>
      <span class="dish__price">CAD$15.25</span>
      <span class="dish__go"><svg width="14" height="14" viewBox="0 0 14 14" fill="none" stroke="#fff" stroke-width="2"><path d="M2 7h10M8 3l4 4-4 4"/></svg></span>
    </article>
    <article class="dish">
      <div class="dish__img" role="img" aria-label="Bowl of pork broth ramen with egg and noodles" style="background:linear-gradient(135deg,#d8b26e,#6a3b1d)"></div>
      <div class="dish__body"><h3>Tonkotsu Ramen</h3><p>Indulge in the ultimate ramen experience with our classic tonkotsu bowl.</p></div>
      <span class="dish__price">CAD$16.95</span>
      <span class="dish__go"><svg width="14" height="14" viewBox="0 0 14 14" fill="none" stroke="#fff" stroke-width="2"><path d="M2 7h10M8 3l4 4-4 4"/></svg></span>
    </article>
    <article class="dish">
      <div class="dish__img" role="img" aria-label="Deep fried crispy pork knuckle" style="background:linear-gradient(135deg,#b8642a,#5a2a10)"></div>
      <div class="dish__body"><h3>Crispy Pata</h3><p>Crispy pata, deep fried pork hock crispy skin with tender meat.</p></div>
      <span class="dish__price">CAD$40.99</span>
      <span class="dish__go"><svg width="14" height="14" viewBox="0 0 14 14" fill="none" stroke="#fff" stroke-width="2"><path d="M2 7h10M8 3l4 4-4 4"/></svg></span>
    </article>
    <article class="dish">
      <div class="dish__img" role="img" aria-label="Golden baked empanadas on a plate" style="background:linear-gradient(135deg,#e0a24e,#8a4d1c)"></div>
      <div class="dish__body"><h3>Baked Empanada</h3><p>Empanada is a flaky baked turnover in the shape of a half moon.</p></div>
      <span class="dish__price">CAD$95.00</span>
      <span class="dish__go"><svg width="14" height="14" viewBox="0 0 14 14" fill="none" stroke="#fff" stroke-width="2"><path d="M2 7h10M8 3l4 4-4 4"/></svg></span>
    </article>
    <article class="dish">
      <div class="dish__img" role="img" aria-label="Plated menu dish" style="background:linear-gradient(135deg,#c98a46,#6b3a18)"></div>
    </article>
  </div>
  <div class="menu__cta"><span class="btn">Order Now</span></div>
</section>

<section class="order">
  <div class="order__photo" role="img" aria-label="Grilled meat skewers on a plate with lime and chili"></div>
  <div class="order__text">
    <h2 class="display">Order <span class="red">Online</span></h2>
    <h3>And Enjoy Anywhere</h3>
    <p>Craving something delicious? Place your order online for pickup or delivery and enjoy your favorites from the comfort of your home.</p>
    <span class="btn btn--light">Order Now</span>
  </div>
  <div class="off-badge">50%<small>OFF</small></div>
</section>

<section class="occasion">
  <div class="occasion__photo" role="img" aria-label="Friends celebrating a birthday with balloons"></div>
  <div class="occasion__body">
    <h2 class="display">Make Every Occasion<br><span class="red">Special</span></h2>
    <p>Planning an event? Let us handle the food while you enjoy the celebration. Our catering services are perfect for:</p>
    <ul class="occasion__list">
      <li>Corporate Events</li><li>Weddings</li><li class="strong">Birthdays</li><li>Family Gatherings</li>
    </ul>
    <p>With flexible packages and a focus on quality, we'll make your event unforgettable.</p>
    <span class="btn">Book Catering Service</span>
  </div>
</section>

<section class="events">
  <h2 class="section-title display">Upcoming Events &amp; <span class="red">Specials</span></h2>
  <p class="events__intro">There's always something happening! Check out our event calendar for the latest pop-ups, live music nights, and seasonal specials.</p>
  <div class="events__grid">
    <article class="post">
      <div class="post__img" role="img" aria-label="Guests sharing food at a festive dinner" style="background:linear-gradient(135deg,#a8683a,#3c2314)"><span class="post__tag">Event</span></div>
      <div class="post__meta"><span>28-06-2025</span><span>By John</span></div>
      <h3>Some Blog Heading Here</h3>
      <p>Lorem ipsum is simply printing typesetting industry lorem ipsum... <b>READ MORE</b></p>
    </article>
    <article class="post">
      <div class="post__img" role="img" aria-label="Platter of plated specials on a table" style="background:linear-gradient(135deg,#7d8a4a,#3a2a18)"><span class="post__tag">Event</span></div>
      <div class="post__meta"><span>28-06-2025</span><span>By John</span></div>
      <h3>Some Blog Heading Here</h3>
      <p>Lorem ipsum is simply printing typesetting industry lorem ipsum... <b>READ MORE</b></p>
    </article>
    <article class="post">
      <div class="post__img" role="img" aria-label="Crowd enjoying a live music night" style="background:linear-gradient(135deg,#8a4a3a,#2a1a18)"><span class="post__tag">Event</span></div>
      <div class="post__meta"><span>28-06-2025</span><span>By John</span></div>
      <h3>Some Blog Heading Here</h3>
      <p>Lorem ipsum is simply printing typesetting industry lorem ipsum... <b>READ MORE</b></p>
    </article>
  </div>
  <div class="events__cta"><span class="btn">View All Events</span></div>
</section>

<section class="social">
  <div class="social__text">
    <h2 class="display">Follow Us <span class="red">Instagram</span></h2>
    <p>Stay connected with us on social media for daily updates, behind-the-scenes moments and exciting announcements.</p>
    <div class="handle"><i></i>@brisatostada</div>
    <div class="handle"><i></i>@nuevosendero</div>
  </div>
  <div class="social__phones" role="img" aria-label="Two smartphones showing the restaurant's social feed"></div>
</section>

<footer class="site-footer">
  <div class="footer__cols">
    <div class="footer__col">
      <h4>Opening Hours</h4>
      <p>Monday to Friday: 9 AM – 9 PM<br>Saturday &amp; Sunday: 9 AM – 7 PM</p>
      <div class="socials"><i></i><i></i><i></i><i></i></div>
    </div>
    <div class="footer__col">
      <h4>Contact Us</h4>
      <p><b>NUEVO SENDERO:</b><br>Pickup: 88 Calle Marea Ave, Toronto ON<br>12 Lantern Row, St Catharines ON<br>1-289-555-0187</p>
      <p style="margin-top:10px"><b>BRISA TOSTADA:</b><br>hola@brisatostada.com</p>
    </div>
    <div class="footer__col">
      <h4>Stay in the Loop</h4>
      <p>Subscribe to our email updates to get the latest news.</p>
      <div class="subscribe"><span>Enter your email...</span><b>SUBSCRIBE</b></div>
    </div>
    <div class="footer__col">
      <h4>Payment</h4>
      <div class="cards"><i></i><i></i><i></i><i></i><i></i><i></i><i></i><i></i></div>
    </div>
  </div>
  <div class="footer__bar">© COPYRIGHT BRISA TOSTADA. ALL RIGHTS RESERVED</div>
</footer>

</body>
</html>
```